Velvet Fern Beauty Bar Business Card

We need a modern, elegant business card design for our new beauty bar located in La Quinta, CA. The card should feel premium yet approachable, reflecting our brand identity: warm, stylish, and confidence-boosting.

Use our existing Velvet Fern Beauty Bar logo (to be provided as vector file).

Colors: Black, White, Blush / Nude accents, and Gold (metallic or foil effect if possible).

Typography: Clean sans-serif for clarity, with optional elegant script accent.
Design Style

Minimalist and modern with plenty of white space.

Premium look with a beauty/lifestyle feel (not overly corporate).

Option to explore vertical or horizontal orientation.

Rounded corners welcome, but not required.

Additional Notes

Design should print well in both matte and glossy finishes.

Please present mockups with both light and dark backgrounds.

Keep overall feel sleek, feminine, and high-end while still being approachable.

```html
<!DOCTYPE html>
<html lang="en">
<head>
<meta charset="utf-8">
<title>Velvet Fern Beauty Bar – Business Card</title>
<link rel="stylesheet" href="https://fonts.googleapis.com/css2?family=Cinzel:wght@400;500&family=Montserrat:wght@400;500&display=swap">
<style>
  :root {
    --backdrop: #3b3b3c;
    --card-light: #ffffff;
    --card-dark: #2d2d2e;
    --rose-gold: #c9886f;
    --rose-edge: #d9a08a;
    --ink: #1d1d1d;
    --divider: #cfcfcf;
  }
  * { margin: 0; padding: 0; box-sizing: border-box; }
  html, body {
    width: 1200px;
    height: 1200px;
    overflow: hidden;
    background: var(--backdrop);
  }
  .sheet {
    width: 1200px;
    height: 1200px;
    display: flex;
    flex-direction: column;
    align-items: center;
    justify-content: center;
    gap: 52px;
  }
  .card {
    position: relative;
    width: 900px;
    height: 514px;
    border-radius: 44px;
    border-bottom: 5px solid var(--rose-edge);
    border-right: 3px solid var(--rose-edge);
    box-shadow: 0 14px 30px rgba(0,0,0,0.35);
  }
  .card--front { background: var(--card-light); }
  .card--back {
    background: var(--card-dark);
    display: flex;
    align-items: center;
    justify-content: center;
  }

  .brand {
    display: flex;
    align-items: center;
    gap: 16px;
    font-family: "Cinzel", serif;
    font-weight: 400;
    color: var(--rose-gold);
    letter-spacing: 0.04em;
    white-space: nowrap;
  }
  .brand__dot {
    width: 16px;
    height: 16px;
    border-radius: 50%;
    background: var(--rose-gold);
    flex: none;
  }
  .card--front .brand {
    position: absolute;
    top: 90px;
    left: 0;
    right: 0;
    justify-content: center;
    font-size: 40px;
  }
  .card--back .brand { font-size: 50px; }

  .identity {
    position: absolute;
    left: 84px;
    top: 290px;
  }
  .identity__name {
    font-family: "Cinzel", serif;
    font-weight: 400;
    font-size: 52px;
    color: var(--rose-gold);
    line-height: 1;
    letter-spacing: 0.02em;
  }
  .identity__title {
    font-family: "Montserrat", sans-serif;
    font-weight: 400;
    font-size: 30px;
    color: var(--ink);
    margin-top: 10px;
    letter-spacing: 0.04em;
  }

  .divider {
    position: absolute;
    left: 475px;
    top: 250px;
    width: 1px;
    height: 170px;
    background: var(--divider);
  }

  .contact {
    position: absolute;
    left: 515px;
    top: 258px;
    list-style: none;
    font-family: "Montserrat", sans-serif;
    font-size: 27px;
    color: var(--ink);
  }
  .contact__item {
    display: flex;
    align-items: center;
    gap: 12px;
    height: 52px;
  }
  .contact__icon { width: 28px; height: 28px; flex: none; }
</style>
</head>
<body>
<main class="sheet">

  <section class="card card--front" aria-label="Card front">
    <div class="brand">
      <span class="brand__dot"></span>
      <span class="brand__name">Velvet Fern Beauty Bar</span>
    </div>

    <div class="identity">
      <p class="identity__name">Full Name</p>
      <p class="identity__title">TITLE</p>
    </div>

    <div class="divider"></div>

    <ul class="contact">
      <li class="contact__item">
        <svg class="contact__icon" viewBox="0 0 24 24" aria-hidden="true">
          <path fill="var(--rose-gold)" d="M6.6 10.8a15.1 15.1 0 0 0 6.6 6.6l2.2-2.2a1 1 0 0 1 1-.25 11.4 11.4 0 0 0 3.6.57 1 1 0 0 1 1 1V20a1 1 0 0 1-1 1A17 17 0 0 1 3 4a1 1 0 0 1 1-1h3.5a1 1 0 0 1 1 1c0 1.25.2 2.45.57 3.57a1 1 0 0 1-.25 1z"/>
        </svg>
        <span>(000) 000 0000</span>
      </li>
      <li class="contact__item">
        <svg class="contact__icon" viewBox="0 0 24 24" aria-hidden="true">
          <rect x="2" y="5" width="20" height="14" rx="1.5" fill="var(--rose-gold)"/>
          <path d="M2.5 6 12 13l9.5-7" fill="none" stroke="#fff" stroke-width="1.6"/>
        </svg>
        <span>email@company.com</span>
      </li>
      <li class="contact__item">
        <svg class="contact__icon" viewBox="0 0 24 24" aria-hidden="true">
          <g fill="none" stroke="var(--rose-gold)" stroke-width="1.6">
            <circle cx="12" cy="12" r="9.5"/>
            <ellipse cx="12" cy="12" rx="4.2" ry="9.5"/>
            <path d="M2.5 12h19M4 7h16M4 17h16"/>
          </g>
        </svg>
        <span>www.company.com</span>
      </li>
    </ul>
  </section>

  <section class="card card--back" aria-label="Card back">
    <div class="brand">
      <span class="brand__dot"></span>
      <span class="brand__name">Velvet Fern Beauty Bar</span>
    </div>
  </section>

</main>
</body>
</html>
```